Website Header for new website

We need a header/banner design for our revised website. Here is the link to our existing website lorimakwell.me and to our new website in process agewiseplus.us
Area of expertise is older adults, baby boomers and caregivers
This is an individual, professional website for a Speaker, Keynoter, Author, Brocaster

Target Market(s)

Event planners, broadcasters, publishers

Font styles to use
Serif

```html
<!DOCTYPE html>
<html lang="en">
<head>
<meta charset="utf-8">
<title>Lori Makwell – Speaker, Broadcaster, Author</title>
<link rel="stylesheet" href="https://fonts.googleapis.com/css2?family=Bitter:ital,wght@0,300;0,400;1,400&display=swap">
<style>
  :root {
    --brand-blue: #4b4ff2;
    --brand-violet: #5a55f0;
    --band-blue: #4a4cf0;
    --text-dark: #2e2e33;
    --text-soft: #3a3a40;
    --white: #ffffff;
    --hall-deep: #5b5a8c;
    --hall-mid: #a9a7c9;
    --hall-light: #e9e8f2;
  }
  * { margin: 0; padding: 0; box-sizing: border-box; }
  html, body { width: 1200px; height: 429px; overflow: hidden; background: var(--white); }
  .header-banner {
    position: relative;
    width: 1200px;
    height: 429px;
    overflow: hidden;
    font-family: "Bitter", Georgia, serif;
  }
  .hall-backdrop {
    position: absolute; inset: 0;
    background:
      radial-gradient(ellipse at 18% 20%, #c9c3ea 0%, transparent 45%),
      radial-gradient(ellipse at 70% 30%, #f4f3f8 0%, transparent 55%),
      linear-gradient(180deg, var(--hall-mid) 0%, var(--hall-deep) 45%, #6f6d93 80%, var(--hall-light) 100%);
  }
  .speaker-portrait {
    position: absolute;
    left: 146px; top: 12px;
    width: 228px; height: 314px;
    border-radius: 110px 110px 20px 20px;
    background: linear-gradient(180deg, #d9b98a 0%, #d9b98a 22%, #e2bfa8 30%, #1f6a73 42%, #165c66 100%);
  }
  .arc-overlay { position: absolute; left: 0; top: 0; }
  .speaker-name {
    position: absolute;
    left: 612px; top: 34px;
    font-weight: 300;
    font-size: 62px;
    letter-spacing: 4px;
    line-height: 1;
    color: var(--brand-violet);
  }
  .role-list {
    position: absolute;
    left: 623px; top: 137px;
    list-style: none;
    display: grid;
    grid-template-columns: 302px 260px;
    row-gap: 6px;
    font-size: 22px;
    line-height: 24px;
    color: var(--text-dark);
  }
  .tagline {
    position: absolute;
    left: 660px; top: 256px;
    width: 475px;
    text-align: center;
    font-style: italic;
    font-size: 15.5px;
    line-height: 24px;
    color: var(--text-soft);
  }
  .featured-band {
    position: absolute;
    left: 0; top: 326px;
    width: 1200px; height: 103px;
    background: var(--band-blue);
    color: var(--white);
  }
  .featured-label {
    position: absolute;
    left: 66px; top: 32px;
    font-size: 31px;
    line-height: 36px;
  }
  .outlet {
    position: absolute;
    top: 38px;
    display: flex;
    align-items: center;
    gap: 7px;
    font-size: 17px;
    line-height: 24px;
    white-space: nowrap;
  }
  .outlet-mark { width: 12px; height: 12px; background: var(--white); }
</style>
</head>
<body>
  <header class="header-banner">
    <div class="hall-backdrop" role="img" aria-label="Blurred conference hall with a seated audience facing a lit stage"></div>
    <div class="speaker-portrait" role="img" aria-label="Portrait of the speaker in a teal dress, seated"></div>

    <svg class="arc-overlay" width="1200" height="326" viewBox="0 0 1200 326" aria-hidden="true">
      <defs>
        <linearGradient id="arcStroke" x1="0" y1="0" x2="0" y2="1">
          <stop offset="0" stop-color="#6a66f4"/>
          <stop offset="1" stop-color="#3f43ee"/>
        </linearGradient>
      </defs>
      <path d="M478,0 C560,55 602,165 588,248 C581,288 566,312 548,326 L1200,326 L1200,0 Z" fill="rgba(255,255,255,0.78)"/>
      <path d="M478,0 C560,55 602,165 588,248 C581,288 566,312 548,326" fill="none" stroke="url(#arcStroke)" stroke-width="20"/>
    </svg>

    <h1 class="speaker-name">LORI MAKWELL</h1>

    <ul class="role-list">
      <li>-Dynamic Keynoter</li>
      <li>-Motivational speaker</li>
      <li>-Influential Broadcaster</li>
      <li>-Prolific Author</li>
      <li>-Entertaining Blogger</li>
      <li>- Effective Trainer</li>
    </ul>

    <p class="tagline">Staff Training, Design, Marketing, Branding to<br>Reach Boomers, the Mature, and Caregivers</p>

    <section class="featured-band">
      <h2 class="featured-label" style="font-weight:400">Featured on:</h2>
      <div class="outlet" style="left:320px"><span class="outlet-mark"></span>Newsline</div>
      <div class="outlet" style="left:474px"><span class="outlet-mark"></span>Eastfield Audio</div>
      <div class="outlet" style="left:632px"><span class="outlet-mark"></span>The Daytime Hour</div>
      <div class="outlet" style="left:812px"><span class="outlet-mark"></span>WKRV The Signal</div>
      <div class="outlet" style="left:990px"><span class="outlet-mark"></span>Trade Talk Radio</div>
    </section>
  </header>
</body>
</html>
```